High end Coffee Roaster needs a Label design for new Blend

We are looking for a label design for a new blend called "Cold Brew Blend". It is a blend of coffee that we use for making cold brew coffee. The blend is sold as the whole bean and ground coffee in a bag as well as pre-brewed ready to drink in a bottle. We would like the label to be elegant but fun and It must include our logo. Please check out or website brightmilebeans.com or social media @brightmilebeans for information on our company and our coffees if you need more ideas on the kind of product we offer and our style.
Updates

Requirements
Must have
• Our Company Logo. Creative design.
Should not have
• This project should NOT be a corporate company logo, Please do NOT submit a design for a company logo this is a project for a Label. We already have a logo and we are looking for a design on a label. I have uploaded several examples of what we are looking for. Those examples are from other coffee companies who have cold brew. Those are examples only to give you a better idea of what im looking for. DO NOT COPY THEM.

```html
<!DOCTYPE html>
<html lang="en">
<head>
<meta charset="utf-8">
<title>Bright Mile Beans – Cold Brew Blend Label Concepts</title>
<link rel="stylesheet" href="https://fonts.googleapis.com/css2?family=Montserrat:wght@400;500;600;800&family=Oswald:wght@300;500&display=swap">
<style>
  :root {
    --board: #222222;
    --paper: #ffffff;
    --frame: #a87a4f;
    --logo-tile: #5a4048;
    --espresso: #3d2214;
    --roast: #6b3a1c;
    --caramel: #c8955f;
    --ink: #1e1a18;
    --ink-light: #4a4442;
  }
  * { margin: 0; padding: 0; box-sizing: border-box; }
  html, body { width: 1200px; height: 800px; overflow: hidden; background: var(--board); }
  .board { position: relative; width: 1200px; height: 800px; }

  .label { position: absolute; top: 122px; width: 492px; height: 492px; background: var(--paper); }
  .label--a { left: 88px; }
  .label--b { left: 605px; }

  .frame { position: absolute; border: 2.4px solid var(--frame); }

  .brand-tile {
    position: absolute; background: var(--logo-tile);
    display: flex; flex-direction: column; align-items: center; justify-content: center; gap: 8px;
  }
  .brand-dot { width: 22px; height: 22px; border-radius: 50%; background: var(--caramel); }
  .brand-name {
    font-family: "Montserrat", sans-serif; font-weight: 600; color: var(--paper);
    letter-spacing: 0.04em; text-align: center; line-height: 1.15;
  }

  .beans { position: absolute; }

  .title {
    position: absolute; font-family: "Montserrat", sans-serif; font-weight: 800;
    line-height: 1; letter-spacing: 0.02em;
  }
  .title span { display: block; }
  .subtitle {
    position: absolute; font-family: "Montserrat", sans-serif; font-weight: 500;
    letter-spacing: 0.2em;
  }

  .specs {
    position: absolute; font-family: "Oswald", sans-serif; font-weight: 300;
    color: var(--ink-light); text-transform: uppercase; white-space: nowrap;
  }
  .specs b { font-weight: 500; color: var(--ink); }

  /* concept A */
  .label--a .frame { left: 14px; top: 14px; width: 465px; height: 463px; }
  .label--a .brand-tile { left: 90px; top: 14px; width: 126px; height: 126px; }
  .label--a .brand-name { font-size: 12px; }
  .label--a .beans { left: 104px; top: 140px; }
  .title-panel { position: absolute; left: 216px; top: 140px; width: 276px; height: 212px; background: var(--espresso); }
  .label--a .title { left: 238px; top: 164px; font-size: 54px; color: var(--paper); line-height: 50px; }
  .label--a .subtitle { left: 239px; top: 313px; font-size: 25px; color: var(--paper); }
  .label--a .rule { position: absolute; left: 392px; top: 322px; width: 105px; height: 2.4px; background: var(--caramel); }
  .label--a .specs { left: 242px; top: 358px; font-size: 10.5px; line-height: 14.4px; }

  /* concept B */
  .label--b .frame { left: 25px; top: 25px; width: 442px; height: 441px; }
  .label--b .brand-tile { left: 193px; top: 0; width: 109px; height: 90px; gap: 6px; }
  .label--b .brand-dot { width: 16px; height: 16px; }
  .label--b .brand-name { font-size: 10px; }
  .label--b .beans { left: 99px; top: 134px; }
  .label--b .title { left: 241px; top: 133px; font-size: 45px; color: var(--roast); line-height: 38px; }
  .label--b .subtitle { left: 242px; top: 245px; font-size: 21px; color: var(--espresso); }
  .label--b .rule { position: absolute; left: 241px; top: 274px; width: 106px; height: 5px; background: var(--caramel); }
  .label--b .specs { left: 240px; top: 289px; font-size: 9.6px; line-height: 14.4px; }

  .caption {
    position: absolute; top: 650px; width: 80px; text-align: center;
    font-family: "Montserrat", sans-serif; font-weight: 600; font-size: 29px; color: var(--paper);
  }
  .caption--a { left: 297px; }
  .caption--b { left: 826px; }
</style>
</head>
<body>
<main class="board">
  <section class="label label--a">
    <div class="frame"></div>
    <div class="brand-tile">
      <div class="brand-dot"></div>
      <div class="brand-name">BRIGHT MILE<br>BEANS</div>
    </div>
    <svg class="beans" width="112" height="220" viewBox="0 0 112 220" role="img" aria-label="Photo of a bowl of dark roasted coffee beans">
      <defs>
        <radialGradient id="beansA" cx="85%" cy="50%" r="80%">
          <stop offset="0" stop-color="#4a2a1a"/>
          <stop offset="0.6" stop-color="#5e3825"/>
          <stop offset="1" stop-color="#2c1810"/>
        </radialGradient>
      </defs>
      <path d="M112 0 A112 110 0 0 0 112 220 Z" fill="url(#beansA)"/>
    </svg>
    <div class="title-panel"></div>
    <h1 class="title"><span>COLD</span><span>BREW</span><span>BLEND</span></h1>
    <div class="subtitle">COFFEE</div>
    <div class="rule"></div>
    <p class="specs">
      <b>Country</b> Ethiopia <b>Region</b> Multiple <b>Farm</b> Multiple<br>
      <b>Growing Elevation</b> 1,700 - 2,000 meters<br>
      <b>Process</b> Wet Process <b>Roast Level</b> Full City<br>
      <b>Tasting Note</b> Rich Chocolate, Black Berry Syrup<br>
      <b>Net Wt</b> 16 oz (145g)
    </p>
  </section>

  <section class="label label--b">
    <div class="frame"></div>
    <div class="brand-tile">
      <div class="brand-dot"></div>
      <div class="brand-name">BRIGHT MILE<br>BEANS</div>
    </div>
    <svg class="beans" width="128" height="216" viewBox="0 0 128 216" role="img" aria-label="Photo of a bowl of dark roasted coffee beans">
      <defs>
        <radialGradient id="beansB" cx="85%" cy="50%" r="80%">
          <stop offset="0" stop-color="#4a2a1a"/>
          <stop offset="0.6" stop-color="#5e3825"/>
          <stop offset="1" stop-color="#2c1810"/>
        </radialGradient>
      </defs>
      <path d="M128 0 A120 108 0 0 0 128 216 Z" fill="url(#beansB)"/>
    </svg>
    <h2 class="title"><span>COLD</span><span>BREW</span><span>BLEND</span></h2>
    <div class="subtitle">COFFEE</div>
    <div class="rule"></div>
    <p class="specs">
      <b>Country</b> Ethiopia <b>Region</b> Multiple <b>Farm</b> Multiple<br>
      <b>Growing Elevation</b> 1,700 - 2,000 meters<br>
      <b>Process</b> Wet Process <b>Roast Level</b> Full City<br>
      <b>Tasting Note</b> Rich Chocolate, Black Berry Syrup<br>
      <b>Net Wt</b> 16 oz (145g)
    </p>
  </section>

  <div class="caption caption--a">1a</div>
  <div class="caption caption--b">1b</div>
</main>
</body>
</html>
```